Deactivated Coal-Fired Power Plant to be redeveloped into a Green Energy Campus.

Want a striking business card statement that introduces our concept project to provide economic and community recovery to a former rural coal community in western PA.
Essentially 12 project representatives that will lead both the demolition of an existing power plant and the redevelopment to a new Green energy site.
Business Card should reflect our effort.
We are open to ideas.

Target Market(s)

Energy and Power Generation industries

Industry/Entity Type

Power Generation and Data Centers

Contact Information for Business Card

Included in uploaded materials

Font styles to use
Sans Serif
Other font styles liked:
• Arial, Calibri

Requirements
Must have
• Multiple colors

```html
<!DOCTYPE html>
<html lang="en">
<head>
<meta charset="utf-8">
<title>Ridgeline Renewal — Business Card</title>
<link href="https://fonts.googleapis.com/css2?family=Roboto:wght@400;700;900&display=swap" rel="stylesheet">
<style>
  :root {
    --stage: #232323;
    --card: #222226;
    --green: #129646;
    --white: #ffffff;
    --text-light: #f2f2f2;
  }
  * { box-sizing: border-box; margin: 0; padding: 0; }
  html, body {
    width: 1200px; height: 780px; overflow: hidden;
    background: var(--stage);
    font-family: "Roboto", Arial, sans-serif;
  }
  .stage {
    position: relative; width: 1200px; height: 780px;
    display: flex; align-items: center; justify-content: center; gap: 40px;
  }
  .card {
    position: relative; width: 540px; height: 309px;
    background: var(--card);
    box-shadow: 0 10px 28px rgba(0,0,0,.55);
    overflow: hidden;
  }
  .brand {
    display: flex; align-items: center; gap: 14px;
    color: var(--white); font-weight: 900; text-transform: uppercase;
    letter-spacing: .02em; line-height: 1;
  }
  .brand__dot { border-radius: 50%; background: var(--green); flex: none; }
  .card--front { display: flex; align-items: center; justify-content: center; }
  .card--front .brand { font-size: 40px; }
  .card--front .brand__dot { width: 64px; height: 64px; }

  .card--back .brand { position: absolute; top: 44px; right: 36px; font-size: 24px; gap: 10px; }
  .card--back .brand__dot { width: 38px; height: 38px; }

  .contact { position: absolute; left: 0; bottom: 30px; }
  .contact__head { position: relative; padding-left: 46px; }
  .contact__bar {
    position: absolute; left: 0; top: 4px; width: 30px; height: 56px; background: var(--green);
  }
  .contact__name { font-size: 32px; font-weight: 900; color: var(--white); line-height: 1.05; }
  .contact__name .first { color: var(--green); }
  .contact__title { font-size: 15px; color: var(--text-light); margin-top: 3px; }
  .contact__company { font-size: 16px; color: var(--green); margin: 10px 0 10px 46px; }
  .contact__list { list-style: none; margin-left: 46px; }
  .contact__item {
    display: flex; align-items: center; gap: 10px;
    font-size: 14.5px; color: var(--text-light); line-height: 1.5;
  }
  .contact__icon { width: 14px; height: 14px; flex: none; }
</style>
</head>
<body>
<main class="stage">
  <section class="card card--front" aria-label="Card front">
    <div class="brand"><span class="brand__dot"></span>Ridgeline Renewal</div>
  </section>

  <section class="card card--back" aria-label="Card back">
    <div class="brand"><span class="brand__dot"></span>Ridgeline Renewal</div>

    <div class="contact">
      <div class="contact__head">
        <span class="contact__bar"></span>
        <h1 class="contact__name"><span class="first">Daniel</span> Porter</h1>
        <p class="contact__title">Chief Operating Officer</p>
      </div>
      <p class="contact__company">Ridgeline Renewal LLC</p>
      <ul class="contact__list">
        <li class="contact__item">
          <svg class="contact__icon" viewBox="0 0 14 14"><rect x="3.5" y="1" width="7" height="12" rx="1.2" fill="none" stroke="#fff" stroke-width="1.4"/></svg>
          555.014.2280
        </li>
        <li class="contact__item">
          <svg class="contact__icon" viewBox="0 0 14 14"><circle cx="7" cy="7" r="6" fill="var(--green)"/><path d="M1 7h12M7 1c-3 3-3 9 0 12M7 1c3 3 3 9 0 12" fill="none" stroke="var(--card)" stroke-width="1"/></svg>
          www.ridgelinerenewal.com
        </li>
        <li class="contact__item">
          <svg class="contact__icon" viewBox="0 0 14 14"><rect x="1" y="3" width="12" height="9" fill="var(--green)"/><path d="M1 3l6 5 6-5" fill="none" stroke="var(--card)" stroke-width="1.2"/></svg>
          dporter@ridgelinerenewal.com
        </li>
      </ul>
    </div>
  </section>
</main>
</body>
</html>
```